Tildens Biscuit Barn Website

I need a website for a diner/restaurant that has been established in a farming, oil and industrial community for over 15 years. The website needs to be simple in design, but that should demonstrate the mastery of skills of the designer. Our diner/restaurant is family oriented, patriotic but very rustic
Fb Address is fb.me/TildensBarn

Pictures of the restaurant

https://www.filecrate-example.net/s/qk72hdw01/Tildens_05.jpg

Pictures of About us

https://www.filecrate-example.net/sh/zm40vrt88/AboutUsPhotos

Article about Tilden's
https://www.filecrate-example.net/s/wp31nbx57/TildensBiscuitBarn1.PDF
https://www.filecrate-example.net/s/hy65lcu29/TildensBiscuitBarn2.PDF

Reason: I was slow to update with information.

Reason: I am just getting feedback to the designs posted. I wasn't sure of the limited feedback was limiting designers from submitting designs. That and running a business with 25 employees open 12 hours a day, being here 2 hours prior and 2-3 hours after makes for long days.

I've increased the first place prize and also added funds to the second and third place prizes for your effort.

I just need the files in PSD, not HTML 5 as originally requested. We can handle getting the coding part.

Ill have the contest finalized by Monday. Thanks for your patience.

Target Market(s)

Cross section of adults from 18-35 & 35-55.

Industry/Entity Type

Industrial

Font styles to use
Other font styles liked:
• ff tisa web pro or garamond premier pro

Requirements
Must have
• Must be clean, look nice and not look like an afterthought.
Nice to have
• Please see the last two documents for information about our restaurant, which was featured in our local newspaper.

```html
<!DOCTYPE html>
<html lang="en">
<head>
<meta charset="utf-8">
<title>Tildens Biscuit Barn</title>
<link rel="stylesheet" href="https://fonts.googleapis.com/css2?family=Cabin:wght@400;600;700&family=EB+Garamond:wght@500;600&display=swap">
<style>
  :root {
    --sky: #f4f4f4;
    --sky-mid: #e4e4e4;
    --sky-deep: #cfcfcf;
    --wood: #4b3d33;
    --wood-light: #5a4a3f;
    --wood-dark: #2c221b;
    --wood-seam: rgba(20, 14, 10, 0.55);
    --teal: #0f4d63;
    --teal-dark: #0a3647;
    --teal-line: #2e7a8e;
    --red: #c41f3b;
    --grey-text: #595959;
    --panel: #221e1c;
    --white: #ffffff;
  }
  * { margin: 0; padding: 0; box-sizing: border-box; }
  html, body { width: 1200px; height: 1000px; overflow: hidden; }
  body {
    position: relative;
    font-family: "Cabin", "Gill Sans", sans-serif;
    background: var(--wood);
  }
  .skyline {
    position: absolute; left: 0; top: 0; width: 1200px; height: 290px;
    background:
      linear-gradient(180deg, rgba(244,244,244,0) 0%, rgba(244,244,244,0) 60%, rgba(200,200,200,0.6) 100%),
      linear-gradient(90deg, var(--sky-mid) 0%, var(--sky) 18%, var(--sky-mid) 30%, var(--sky) 45%, var(--sky) 60%, var(--sky-mid) 75%, var(--sky) 85%, var(--sky-mid) 100%);
  }
  .wood-floor {
    position: absolute; left: 0; top: 290px; width: 1200px; height: 710px;
    background:
      linear-gradient(90deg, rgba(20,14,10,0.45) 0%, rgba(20,14,10,0) 18%, rgba(20,14,10,0) 82%, rgba(20,14,10,0.45) 100%),
      repeating-linear-gradient(90deg, var(--wood-seam) 0px, var(--wood-seam) 2px, var(--wood) 2px, var(--wood-light) 36px, var(--wood) 70px, var(--wood) 72px);
  }
  .info {
    position: absolute; top: 98px; width: 300px; text-align: center;
    text-transform: uppercase;
  }
  .info-label { font-size: 19px; color: var(--grey-text); line-height: 22px; }
  .info-value { font-size: 19px; font-weight: 700; color: var(--red); line-height: 24px; letter-spacing: 0.3px; }
  .info--hours { left: 191px; }
  .info--hours .info-value { font-size: 20px; letter-spacing: 1.1px; }
  .info--order { left: 697px; }
  .info--order .info-label { font-size: 20px; letter-spacing: 0.2px; }
  .info--order .info-value { letter-spacing: 1px; }
  .brand {
    position: absolute; left: 500px; top: 60px; width: 200px; height: 140px;
    display: flex; align-items: center; justify-content: center; gap: 10px;
  }
  .brand-dot { width: 14px; height: 14px; border-radius: 50%; background: var(--red); }
  .brand-name { font-size: 42px; font-weight: 700; color: var(--red); }
  .ribbon { position: absolute; left: 0; top: 238px; width: 1200px; height: 80px; }
  .main-nav {
    position: absolute; left: 0; top: 240px; width: 1200px; height: 53px;
  }
  .main-nav a {
    position: absolute; top: 16px;
    color: var(--white); text-decoration: none; font-size: 18px; line-height: 22px;
    text-transform: uppercase;
  }
  .nav-food { left: 226px; }
  .nav-about { left: 341px; }
  .nav-community { left: 535px; }
  .nav-gallery { left: 711px; }
  .nav-location { left: 858px; }
  .hero {
    position: absolute; left: 150px; top: 292px; width: 896px; height: 530px;
    overflow: hidden;
  }
  .hero-photo {
    position: absolute; inset: 0;
    background:
      radial-gradient(ellipse 44% 30% at 42% 58%, #9a6536 0%, #b98650 45%, rgba(214,190,160,0) 100%),
      radial-gradient(ellipse 62% 52% at 48% 62%, #ece4d6 0%, #e6dccb 70%, rgba(225,220,212,0) 100%),
      linear-gradient(180deg, #d0d0d0 0%, #dcdad5 40%, #d6d3ce 100%);
  }
  .hero-caption {
    position: absolute; left: 492px; top: 328px; width: 404px; height: 129px;
    background: var(--red); color: var(--white); text-align: center;
    padding-top: 35px;
  }
  .hero-title {
    font-family: "EB Garamond", Georgia, serif; font-weight: 600;
    font-size: 30px; letter-spacing: 1px; line-height: 32px; text-transform: uppercase;
  }
  .hero-sub { font-size: 17.5px; line-height: 22px; }
  .hero-dots {
    position: absolute; left: 377px; top: 487px; display: flex; gap: 20px;
  }
  .hero-dots span { width: 21px; height: 21px; border-radius: 50%; background: rgba(120,120,120,0.75); }
  .hero-dots span.is-active { background: rgba(235,235,235,0.9); }
  .intro-panel {
    position: absolute; left: 150px; top: 878px; width: 896px; height: 122px;
    background: var(--panel);
  }
  .intro-title {
    position: absolute; left: 43px; top: 30px;
    font-family: "EB Garamond", Georgia, serif; font-weight: 500;
    font-size: 39px; line-height: 50px; letter-spacing: 1.2px; color: var(--white); text-transform: uppercase;
  }
  .intro-rule { position: absolute; left: 20px; top: 80px; width: 856px; height: 16px; }
  .intro-icon { position: absolute; left: 776px; top: 17px; }
</style>
</head>
<body>
  <div class="skyline" role="img" aria-label="Faint illustration of an oil refinery skyline"></div>
  <div class="wood-floor" role="img" aria-label="Weathered vertical wood plank texture"></div>

  <div class="info info--hours">
    <div class="info-label">Hours Open</div>
    <div class="info-value">Everyday 5AM - 2PM</div>
  </div>

  <div class="brand">
    <span class="brand-dot"></span>
    <span class="brand-name">Tilden's</span>
  </div>

  <div class="info info--order">
    <div class="info-label">Call an order to go!</div>
    <div class="info-value">(555) 014-2273</div>
  </div>

  <svg class="ribbon" viewBox="0 0 1200 80" aria-hidden="true">
    <polygon points="28,24 85,24 85,76 60,72 14,76 36,50" fill="var(--teal-dark)"/>
    <polygon points="1172,24 1111,24 1111,76 1140,72 1186,76 1162,50" fill="var(--teal-dark)"/>
    <polygon points="85,55 85,76 60,72" fill="#06232f"/>
    <polygon points="1111,55 1111,76 1140,72" fill="#06232f"/>
    <rect x="85" y="2" width="1026" height="53" fill="var(--teal)"/>
  </svg>
  <nav class="main-nav">
    <a class="nav-food" href="#">Food</a>
    <a class="nav-about" href="#">About Tilden's</a>
    <a class="nav-community" href="#">Community</a>
    <a class="nav-gallery" href="#">Gallery</a>
    <a class="nav-location" href="#">Location</a>
  </nav>

  <section class="hero">
    <div class="hero-photo" role="img" aria-label="Plate of powdered sugar French toast with butter, syrup and a small American flag"></div>
    <div class="hero-caption">
      <div class="hero-title">Freedom Toast</div>
      <div class="hero-sub">Always served with an American Flag</div>
    </div>
    <div class="hero-dots">
      <span class="is-active"></span><span></span><span></span><span></span>
    </div>
  </section>

  <section class="intro-panel">
    <h1 class="intro-title">Good Food, and Lots of It!</h1>
    <svg class="intro-icon" width="40" height="58" viewBox="0 0 40 58" aria-hidden="true">
      <g fill="none" stroke="var(--teal-line)" stroke-width="2.5" stroke-linecap="round">
        <path d="M4 2 V16 Q4 22 10 22 Q16 22 16 16 V2"/>
        <path d="M10 2 V56"/>
        <path d="M30 56 V4 Q38 14 36 32 H30"/>
      </g>
    </svg>
    <svg class="intro-rule" viewBox="0 0 856 16" aria-hidden="true">
      <line x1="0" y1="3" x2="856" y2="3" stroke="var(--teal-line)" stroke-width="2"/>
      <line x1="0" y1="14" x2="856" y2="14" stroke="var(--teal-line)" stroke-width="2"/>
    </svg>
  </section>
</body>
</html>
```